FERNHOLT CONSTRUCTION Van Wrap Design

Fernholt construction is looking for a new vehicle wrap for our trade vans
Needs to have our LOGO, PHONE NUMBER (02786450317) QTC LOGO, CRAFT GUILDSMEN LOGO
Something big bold and attractive. The windows are tinted black but could be wrapped in white to continue the design
I have attached some ideas - we would like half wrap or full wrap

(I have attached our OLD van wrap with our OLD logo only for reference - do not copy as this is outdated)

```html
<!DOCTYPE html>
<html lang="en">
<head>
<meta charset="utf-8">
<title>Fernholt Construction – Van Wrap</title>
<link rel="stylesheet" href="https://fonts.googleapis.com/css2?family=Montserrat:wght@500;600;700&family=Saira:wght@600;700&display=swap">
<style>
  :root{
    --bg:#e6e7e9;
    --white:#ffffff;
    --black:#1c1c1d;
    --red:#e21a22;
    --grey:#6d6e70;
    --tree-light:#9a9a9a;
    --tree-dark:#3a3a3a;
  }
  *{margin:0;padding:0;box-sizing:border-box}
  html,body{width:1200px;height:1200px;overflow:hidden;background:var(--bg)}
  .canvas{position:relative;width:1200px;height:1200px}

  .wrap-panel{position:absolute;left:40px;width:1120px;border-radius:28px;overflow:hidden;box-shadow:0 6px 20px rgba(0,0,0,.12)}
  .wrap-panel svg.shapes{position:absolute;inset:0;width:100%;height:100%}
  .side-panel{top:40px;height:500px}
  .rear-panel{top:600px;height:560px}

  .logo{position:absolute;display:flex;align-items:center;gap:22px}
  .logo-mark{width:110px;height:190px;border-radius:4px}
  .side-panel .logo-mark{background:linear-gradient(180deg,var(--tree-light),var(--tree-dark))}
  .rear-panel .logo-mark{background:linear-gradient(180deg,#f2f2f2,#bdbdbd)}
  .logo-name{font-family:"Montserrat",sans-serif;font-weight:600;letter-spacing:.22em;line-height:1.15}
  .logo-name span{display:block}
  .side-panel .logo{left:150px;top:200px}
  .side-panel .logo-name{color:var(--black);font-size:40px}
  .rear-panel .logo{left:310px;top:50px}
  .rear-panel .logo-name{color:var(--white);font-size:38px}

  .phone{position:absolute;font-family:"Saira",sans-serif;font-weight:700;color:var(--white);letter-spacing:.02em}
  .phone::before{content:"("}
  .phone::after{content:")"}
  .side-panel .phone{right:70px;top:78px;font-size:50px}
  .rear-panel .phone{left:150px;top:312px;font-size:44px}

  .web-pill{position:absolute;background:var(--red);border-radius:30px;font-family:"Saira",sans-serif;font-weight:700;color:var(--black);letter-spacing:.01em;text-align:center}
  .side-panel .web-pill{right:60px;top:160px;padding:8px 28px;font-size:26px}
  .rear-panel .web-pill{left:560px;top:318px;padding:9px 26px;font-size:24px}

  .badges{position:absolute;display:flex;align-items:center;gap:18px}
  .badge-square{width:62px;height:74px;background:linear-gradient(180deg,#888,#2a2a2a);border-radius:3px}
  .badge-circle{width:80px;height:80px;border-radius:50%;border:4px solid var(--black);background:var(--white)}
  .side-panel .badges{right:70px;top:350px}
  .rear-panel .badges{right:40px;top:440px}

  .social{position:absolute;left:150px;top:470px;display:flex;gap:14px}
  .social span{width:40px;height:40px;border-radius:6px;background:var(--black)}
</style>
</head>
<body>
<main class="canvas">

  <section class="wrap-panel side-panel" aria-label="Side wrap">
    <svg class="shapes" viewBox="0 0 1120 500" preserveAspectRatio="none">
      <rect width="1120" height="500" fill="var(--white)"/>
      <path d="M560 0 C600 200 760 330 1120 360 L1120 0 Z" fill="var(--red)"/>
      <path d="M610 0 C650 180 790 300 1120 325 L1120 0 Z" fill="var(--black)"/>
      <rect y="470" width="1120" height="30" fill="var(--black)"/>
    </svg>
    <div class="logo">
      <div class="logo-mark" role="img" aria-label="Tree silhouette emblem"></div>
      <div class="logo-name"><span>FERNHOLT</span><span>CONSTRUCTION</span></div>
    </div>
    <div class="phone">02786450317</div>
    <div class="web-pill">FERNHOLTCONSTRUCTION.COM</div>
    <div class="badges">
      <div class="badge-square" role="img" aria-label="Craft Guildsmen membership badge"></div>
      <div class="badge-circle" role="img" aria-label="QTC licence badge"></div>
    </div>
  </section>

  <section class="wrap-panel rear-panel" aria-label="Rear wrap">
    <svg class="shapes" viewBox="0 0 1120 560" preserveAspectRatio="none">
      <rect width="1120" height="560" fill="var(--white)"/>
      <path d="M0 0 H1120 V360 C900 380 760 400 560 470 C380 530 200 460 0 420 Z" fill="var(--red)"/>
      <path d="M0 0 H1120 V330 C900 350 760 370 560 440 C380 500 200 430 0 390 Z" fill="var(--black)"/>
      <rect y="530" width="1120" height="30" fill="var(--black)"/>
    </svg>
    <div class="logo">
      <div class="logo-mark" role="img" aria-label="Tree silhouette emblem"></div>
      <div class="logo-name"><span>FERNHOLT</span><span>CONSTRUCTION</span></div>
    </div>
    <div class="phone">02786450317</div>
    <div class="web-pill">FERNHOLTCONSTRUCTION.COM</div>
    <div class="social" aria-label="Social media">
      <span></span><span></span>
    </div>
    <div class="badges">
      <div class="badge-circle" role="img" aria-label="QTC licence badge"></div>
      <div class="badge-square" role="img" aria-label="Craft Guildsmen membership badge"></div>
    </div>
  </section>

</main>
</body>
</html>
```